Marchesi Orthodontics
Business Card / Stationary Design
Professional
Lucia Marchesi
Orthodontist
4817 W. Harborview Ave. Suite 204
Fort Lauderdale, FL 33419
marchesiortho@mailvexo.com
www.pinegrovesmiles.com

```html
<!DOCTYPE html>
<html lang="en">
<head>
<meta charset="utf-8">
<title>Marchesi Orthodontics – Business Card Set</title>
<link rel="stylesheet" href="https://fonts.googleapis.com/css2?family=Montserrat:wght@400;600;700&display=swap">
<style>
  :root {
    --brand-blue: #3a8fd6;
    --brand-blue-dark: #2f7dc2;
    --ink: #4a4a4a;
    --rule-grey: #c9ccd0;
    --charcoal: #3a3a3a;
    --paper: #ffffff;
    --page: #ffffff;
  }
  * { margin: 0; padding: 0; box-sizing: border-box; }
  html, body { width: 1200px; height: 722px; overflow: hidden; background: var(--page); }
  body { position: relative; font-family: "Montserrat", Arial, sans-serif; }

  .card {
    position: absolute;
    width: 557px;
    height: 312px;
    overflow: hidden;
    box-shadow: 0 0 0 1px #d5d7da;
  }
  .card--front { left: 24px; top: 24px; background: var(--paper); }
  .card--logo-white { left: 619px; top: 24px; background: var(--paper); }
  .card--logo-charcoal { left: 24px; top: 365px; background: var(--charcoal); }
  .card--logo-blue { left: 619px; top: 365px; background: var(--brand-blue); }

  .card__shapes { position: absolute; inset: 0; }

  .wordmark {
    position: absolute;
    display: flex;
    align-items: center;
    gap: 10px;
    font-weight: 700;
    letter-spacing: 3px;
    line-height: 1.05;
    text-transform: uppercase;
  }
  .wordmark__dot { width: 14px; height: 14px; border-radius: 50%; flex: none; }
  .wordmark__name { font-size: 34px; display: block; }
  .wordmark__sub { font-size: 34px; display: block; }
  .wordmark--compact .wordmark__name,
  .wordmark--compact .wordmark__sub { font-size: 26px; }

  .wordmark--blue { color: var(--brand-blue); }
  .wordmark--blue .wordmark__dot { background: var(--brand-blue); }
  .wordmark--white { color: #ffffff; }
  .wordmark--white .wordmark__dot { background: #ffffff; }

  .front__wordmark { left: 38px; top: 138px; }
  .centered-wordmark { left: 50%; top: 50%; transform: translate(-50%, -55%); }

  .person { position: absolute; right: 30px; top: 20px; text-align: right; }
  .person__name { color: var(--brand-blue); font-weight: 600; font-size: 14px; }
  .person__role { color: var(--ink); font-size: 10px; margin-top: 2px; }

  .contact {
    position: absolute; left: 38px; top: 232px;
    font-size: 10.5px; color: var(--ink); line-height: 1.45;
  }
  .contact__label { color: var(--brand-blue); font-weight: 700; display: inline-block; width: 12px; }

  .website {
    position: absolute; right: 24px; bottom: 12px;
    font-size: 10.5px; color: #ffffff;
  }
  .website--centered { left: 0; right: 0; bottom: 22px; text-align: center; }
</style>
</head>
<body>

  <section class="card card--front" aria-label="Business card front">
    <svg class="card__shapes" width="557" height="312" viewBox="0 0 557 312" aria-hidden="true">
      <path d="M0,0 H470 C330,18 150,60 0,150 Z" fill="var(--brand-blue)"/>
      <path d="M0,154 C150,64 330,22 480,4" fill="none" stroke="var(--rule-grey)" stroke-width="3"/>
      <path d="M557,262 C450,270 330,292 250,312 H557 Z" fill="var(--brand-blue)"/>
    </svg>

    <div class="person">
      <p class="person__name">Lucia Marchesi</p>
      <p class="person__role">Orthodontist</p>
    </div>

    <div class="wordmark wordmark--blue front__wordmark">
      <span class="wordmark__dot"></span>
      <span><span class="wordmark__name">Marchesi</span><span class="wordmark__sub">Orthodontics</span></span>
    </div>

    <address class="contact" style="font-style:normal">
      <p>4817 W. Harborview Ave. Suite 204</p>
      <p>Fort Lauderdale, FL 33419</p>
      <p><span class="contact__label">P</span>: 9545550182</p>
      <p><span class="contact__label">F</span>: 9545550147</p>
      <p><span class="contact__label">E</span>: marchesiortho@mailvexo.com</p>
    </address>

    <p class="website">www.pinegrovesmiles.com</p>
  </section>

  <section class="card card--logo-white" aria-label="Business card back, white">
    <div class="wordmark wordmark--blue wordmark--compact centered-wordmark">
      <span class="wordmark__dot"></span>
      <span><span class="wordmark__name">Marchesi</span><span class="wordmark__sub">Orthodontics</span></span>
    </div>
  </section>

  <section class="card card--logo-charcoal" aria-label="Business card back, charcoal">
    <div class="wordmark wordmark--white wordmark--compact centered-wordmark">
      <span class="wordmark__dot"></span>
      <span><span class="wordmark__name">Marchesi</span><span class="wordmark__sub">Orthodontics</span></span>
    </div>
    <p class="website website--centered">www.pinegrovesmiles.com</p>
  </section>

  <section class="card card--logo-blue" aria-label="Business card back, blue">
    <div class="wordmark wordmark--white wordmark--compact centered-wordmark">
      <span class="wordmark__dot"></span>
      <span><span class="wordmark__name">Marchesi</span><span class="wordmark__sub">Orthodontics</span></span>
    </div>
    <p class="website website--centered">www.pinegrovesmiles.com</p>
  </section>

</body>
</html>
```